Double-sided Business card design needed

I work as an independent consultant in a range of fields, and I need a business card to describes the two main business operations in a two-sided format:

(1) HOPE - Health Outreach Peer Engagement

(2) ROOT - Restoring Original Territories Together

My personal profile so far has been describing myself as:
Dr Calvin Marsh- Independent R&D Consultant in Community Wellbeing, Education, Mental Health and Disability Support Reform

Industry/Entity Type

Business

Contact Information for Business Card

I need a double-sided business card, describing two different but related businesses that I operate: one in Disability & Mental Health, Education and Community Wellbeing consulting, teaching and research; the other in Indigenous/First Nations-specific community cultural development

Logo Text

See the two business names below for logo text - and they need two different logo designs

Logo styles of interest
Pictorial/Combination Logo

```html
<!DOCTYPE html>
<html lang="en">
<head>
<meta charset="utf-8">
<title>Dr Calvin Marsh – Double-sided Business Card</title>
<link rel="stylesheet" href="https://fonts.googleapis.com/css2?family=Michroma&family=Roboto+Condensed:wght@400&family=Inter:wght@300&display=swap">
<style>
  :root {
    --backdrop: #8d8d8d;
    --card-paper: #efebd8;
    --ink: #1c1c1c;
    --root-red: #d93a2b;
    --hope-green: #1b8a5e;
    --band-text: #f7f3e6;
    --label-ink: #111111;
  }
  * { box-sizing: border-box; margin: 0; padding: 0; }
  html, body { width: 1200px; height: 800px; overflow: hidden; }
  body { background: var(--backdrop); }

  .canvas { position: relative; width: 1200px; height: 800px; }

  .side-label {
    position: absolute;
    font-family: "Inter", sans-serif;
    font-weight: 300;
    font-size: 60px;
    color: var(--label-ink);
    letter-spacing: -0.5px;
  }
  .side-label--a { left: 655px; top: 160px; }
  .side-label--b { left: 345px; top: 520px; }

  .card {
    position: absolute;
    width: 500px;
    height: 290px;
    background: var(--card-paper);
    display: flex;
    flex-direction: column;
    box-shadow: 0 6px 14px rgba(0,0,0,0.25);
  }
  .card--root { left: 100px; top: 90px; }
  .card--hope { left: 620px; top: 430px; }

  .card__brand {
    padding-top: 22px;
    text-align: center;
  }
  .brand-name {
    font-family: "Michroma", sans-serif;
    font-size: 26px;
    letter-spacing: 3px;
    line-height: 1;
  }
  .card--root .brand-name { color: var(--root-red); }
  .card--hope .brand-name { color: var(--hope-green); }

  .brand-tagline {
    margin-top: 8px;
    font-family: "Michroma", sans-serif;
    font-size: 10px;
    letter-spacing: 1px;
    color: var(--ink);
    text-transform: uppercase;
  }

  .card__holder {
    flex: 1;
    display: flex;
    align-items: center;
    justify-content: center;
    font-family: "Michroma", sans-serif;
    font-size: 22px;
    letter-spacing: 3px;
    color: var(--ink);
    text-transform: uppercase;
  }

  .card__band {
    height: 88px;
    display: flex;
    align-items: center;
    font-family: "Roboto Condensed", sans-serif;
    color: var(--band-text);
  }
  .card--root .card__band {
    background: var(--root-red);
    justify-content: space-between;
    padding: 0 36px;
    font-size: 17px;
  }
  .card--hope .card__band {
    background: var(--hope-green);
    justify-content: center;
    text-align: center;
    font-size: 14.5px;
    line-height: 1.35;
    padding: 0 40px;
  }

  .contact { display: flex; align-items: center; gap: 7px; }
  .contact--phone { align-self: flex-end; margin-bottom: 20px; }
  .contact--email { align-self: flex-start; margin-top: 20px; }
  .contact__icon { width: 16px; height: 16px; fill: none; stroke: var(--ink); stroke-width: 1.6; }
  .contact__icon--solid { fill: var(--ink); stroke: none; }
</style>
</head>
<body>
<main class="canvas">

  <section class="card card--root" aria-label="Side A – ROOT">
    <header class="card__brand">
      <div class="brand-name">ROOT</div>
      <div class="brand-tagline">Restoring Original Territories Together</div>
    </header>
    <div class="card__holder">Dr Calvin Marsh</div>
    <footer class="card__band">
      <span class="contact contact--phone">
        <svg class="contact__icon contact__icon--solid" viewBox="0 0 24 24" aria-hidden="true">
          <path d="M6.6 10.8a15.2 15.2 0 0 0 6.6 6.6l2.2-2.2a1 1 0 0 1 1-.25 11.4 11.4 0 0 0 3.6.57 1 1 0 0 1 1 1V20a1 1 0 0 1-1 1A17 17 0 0 1 3 4a1 1 0 0 1 1-1h3.5a1 1 0 0 1 1 1c0 1.25.2 2.45.57 3.6a1 1 0 0 1-.25 1z"/>
        </svg>
        01 98765432
      </span>
      <span class="contact contact--email">
        <svg class="contact__icon" viewBox="0 0 24 24" aria-hidden="true">
          <path d="M3 10l9-6 9 6v10H3z"/>
          <path d="M3 10l9 6 9-6"/>
        </svg>
        hello@calvinmarsh.net
      </span>
    </footer>
  </section>

  <div class="side-label side-label--a">Side A</div>
  <div class="side-label side-label--b">Side B</div>

  <section class="card card--hope" aria-label="Side B – HOPE">
    <header class="card__brand">
      <div class="brand-name">HOPE</div>
      <div class="brand-tagline">Health Outreach Peer Engagement</div>
    </header>
    <div class="card__holder">Dr Calvin Marsh</div>
    <footer class="card__band">
      <p>Independent R&amp;D Consultant in Community Wellbeing,<br>Education, Mental Health and Disability Support Reform</p>
    </footer>
  </section>

</main>
</body>
</html>
```